4Star Hotel looking for web design

Hello everyone,
We are located in Cambodia, the hotel should open in 2-3 months. The name will be Velmora-Boutique Hotel. We are looking for a webdesign which is professional, elegant and SIMPLE.
All informations should be easy to find. We are quite open to proposition but we would like to the home page:
-a carousel with around 5-8 picture
-Little menu where we can book a room
By the way, we would like a page for our restaurant, gallery, contact page for description of the rooms. I add some old pictures.
I give an example of what we are expecting:
www.quenrostays.com/tovelspring
We hope that we are proposing a good job for you guys. Have fun and Thanks.
Oh and the winner ( or someone he had choose) of course have free night in our presidential suite
Target Market(s)
We are looking for european Market. Let s say people middle age who are willing to travel in difficult area
Industry/Entity Type
Hotel
Coding
Coded - Design and coding required
Number of Pages Required
5+ page
Requirements
Must have
- Simple, simple and Simple
- Carousel
- place for book a room
- during booking, a menu for select room , and after that another menu for propose like tour in town, taxi, flower, bottle of champagne for example
- during all the process, the customer should be able to know at what step it is and can stop and come back after
- Have to be perfect for smartphone
- Price with drawbar for they know how much they earn with our reduction
Nice to have
- during the process of information (name, adress, tel...), it would be great if they can fill it with a button facebook, google plus, lindkdin, instagram ....
- then a button share on facebook, twitter for know that they book in our hotel
- At the end of the booking, a flashcode with the recapitulatif that customer can scan.

```html
<!DOCTYPE html>
<html lang="en">
<head>
<meta charset="utf-8">
<title>Velmora-Boutique Hotel — Accommodation</title>
<link href="https://fonts.googleapis.com/css2?family=Cinzel:wght@400;700&family=Open+Sans:wght@400;600;700&display=swap" rel="stylesheet">
<style>
:root{
  --maroon:#5b1a17;
  --maroon-dark:#3e0f0d;
  --nav:#6e211c;
  --accent:#e08a2c;
  --title:#c4492a;
  --page:#ebe8e4;
  --panel:#ffffff;
  --text:#6b6b6b;
  --rule:#dedad5;
  --footer:#3a1412;
  --footer-text:#c9b6b2;
}
*{box-sizing:border-box;margin:0;padding:0}
html,body{width:720px;height:1200px;overflow:hidden}
body{position:relative;background:var(--page);font-family:"Open Sans",Arial,sans-serif;color:var(--text)}
.hero{position:absolute;left:0;top:0;width:720px;height:200px;background:linear-gradient(180deg,#6d8fa6 0%,#8aa6b4 35%,#6c7d5a 65%,#8a6f55 100%)}
.topbar{position:absolute;left:0;top:0;width:720px;height:30px;background:rgba(62,15,13,.85)}
.toplinks{position:absolute;right:175px;top:10px;font-size:7px;color:#e6d6d2}
.social{position:absolute;right:90px;top:8px;display:flex;gap:4px}
.social span{width:13px;height:13px;border-radius:50%;background:#c9b8b4}
.logo{position:absolute;left:90px;top:0;width:84px;height:74px;background:#fff;border-bottom:3px solid var(--accent);display:flex;flex-direction:column;align-items:center;justify-content:center;gap:4px;z-index:3;box-shadow:0 2px 4px rgba(0,0,0,.3)}
.logo .mark{width:16px;height:16px;background:var(--maroon)}
.logo .name{font-family:"Cinzel",Georgia,serif;font-size:8.5px;font-weight:700;color:var(--maroon);text-align:center;line-height:1.2}
.nav{position:absolute;left:0;top:30px;width:720px;height:24px;background:var(--nav)}
.nav ul{list-style:none;display:flex;position:absolute;left:186px;top:0;height:24px}
.nav li{font-family:"Cinzel",Georgia,serif;font-size:8px;font-weight:700;color:#f1e3df;padding:0 11px;line-height:24px}
.nav li.active{color:var(--accent)}
.subbar{position:absolute;left:0;top:54px;width:720px;height:18px;background:rgba(91,26,23,.9);font-size:6.5px;color:#e6d6d2}
.subbar span{position:absolute;top:5px;white-space:nowrap}
.sub-address{left:314px}
.sub-reserve{left:445px}
.sub-tel{left:540px}
.dropdown{position:absolute;left:222px;top:54px;width:82px;background:#f4efe9;z-index:2;box-shadow:0 2px 4px rgba(0,0,0,.25)}
.dropdown div{font-size:6.5px;color:#555;padding:4px 8px;border-bottom:1px solid var(--rule)}
.panel{position:absolute;left:90px;top:190px;width:540px;height:850px;background:var(--panel);padding:18px 20px;box-shadow:0 0 4px rgba(0,0,0,.12)}
.page-title{font-family:"Cinzel",Georgia,serif;font-size:12px;font-weight:700;color:var(--maroon);padding-bottom:6px;border-bottom:1px solid var(--rule);margin-bottom:14px}
.room{display:flex;height:131px;border-bottom:1px dotted var(--rule);padding-top:10px}
.room:last-child{border-bottom:none}
.room-photo{width:92px;height:80px;flex:none;border:2px solid #eee}
.room-body{width:190px;margin-left:10px}
.room-name{font-family:"Cinzel",Georgia,serif;font-size:10.5px;color:var(--title);margin-bottom:5px}
.room-text{font-size:6.2px;line-height:1.55}
.room-types{margin-left:auto;width:188px;display:flex;justify-content:flex-end;gap:10px;border-left:1px solid var(--rule);padding-left:8px}
.type{width:52px;text-align:center}
.type-label{font-family:"Cinzel",Georgia,serif;font-size:7px;color:var(--maroon);margin-bottom:5px}
.type-photo{width:52px;height:40px}
.type-btn{display:inline-block;margin-top:4px;background:var(--nav);color:#fff;font-size:5.5px;font-weight:700;padding:2px 8px}
.type-btn.hot{background:var(--accent)}
.footer{position:absolute;left:0;top:1045px;width:720px;height:155px;background:var(--footer);color:var(--footer-text)}
.fcol{position:absolute;top:12px;width:160px}
.fcol h3{font-family:"Cinzel",Georgia,serif;font-size:9px;font-weight:400;color:#f1e3df;margin-bottom:8px}
.fcol p{font-size:6.3px;line-height:1.6}
.post{display:flex;gap:6px;margin-bottom:8px}
.post .thumb{width:26px;height:22px;flex:none}
.post b{display:block;color:var(--accent);font-size:6.3px}
.fbox{background:#fff;width:170px;height:100px;padding:5px}
.fbox .banner{height:40px;background:linear-gradient(90deg,#7a5a3e,#a88a63)}
.fbox .caption{font-size:6px;color:#444;margin:4px 0}
.fbox .faces{display:flex;gap:3px}
.fbox .faces span{width:18px;height:18px;background:#cfc8c2}
.copyright{position:absolute;left:0;bottom:0;width:720px;height:20px;background:var(--maroon-dark);text-align:center;font-size:6px;line-height:20px;color:var(--footer-text)}
</style>
</head>
<body>
<div class="hero" role="img" aria-label="Photo of the hotel grounds with lake and hills"></div>
<div class="topbar">
  <div class="toplinks">Login | Contact | Gallery</div>
  <div class="social"><span></span><span></span><span></span><span></span><span></span></div>
</div>
<div class="logo"><div class="mark"></div><div class="name">Velmora<br>Boutique Hotel</div></div>
<nav class="nav"><ul>
  <li>Home</li><li class="active">Accommodation</li><li>Restaurant &amp; Bar</li><li>Meetings &amp; Events</li><li>Blog</li>
</ul></nav>
<div class="subbar">
  <span class="sub-address">Address: 12 Lantern Lane, Tovel Hill</span>
  <span class="sub-reserve">Reservation</span>
  <span class="sub-tel">Tel: +855 12 345 678</span>
</div>
<div class="dropdown">
  <div>Deluxe Room</div><div>Standard Room</div><div>Family Room</div><div>Junior Suite</div><div>Suite</div>
</div>

<main class="panel">
  <h1 class="page-title">Accommodation</h1>

  <section class="room">
    <div class="room-photo" role="img" aria-label="Standard room photo" style="background:linear-gradient(135deg,#c9a47a,#8a5a3a)"></div>
    <div class="room-body"><h2 class="room-name">Standard Room</h2><p class="room-text">Spacious and calm, this room opens onto the garden terrace with natural light through the day. Hand-finished teak furniture, soft linens and a rain shower bring comfort after long journeys across the province. Breakfast is served daily on the veranda.</p></div>
    <div class="room-types">
      <div class="type"><div class="type-label">Single</div><div class="type-photo" role="img" aria-label="Single room photo" style="background:linear-gradient(135deg,#d8c2a2,#9a7350)"></div><span class="type-btn">DETAILS</span></div>
      <div class="type"><div class="type-label">Twin</div><div class="type-photo" role="img" aria-label="Twin room photo" style="background:linear-gradient(135deg,#d2b894,#8e6440)"></div><span class="type-btn hot">DETAILS</span></div>
      <div class="type"><div class="type-label">Double</div><div class="type-photo" role="img" aria-label="Double room photo" style="background:linear-gradient(135deg,#ccb08a,#7d5535)"></div><span class="type-btn">DETAILS</span></div>
    </div>
  </section>

  <section class="room">
    <div class="room-photo" role="img" aria-label="Deluxe room photo" style="background:linear-gradient(135deg,#e4d8c6,#a08466)"></div>
    <div class="room-body"><h2 class="room-name">Deluxe Room</h2><p class="room-text">Spacious and calm, this room opens onto the garden terrace with natural light through the day. Hand-finished teak furniture, soft linens and a rain shower bring comfort after long journeys across the province. Breakfast is served daily on the veranda.</p></div>
    <div class="room-types">
      <div class="type"><div class="type-label">Single</div><div class="type-photo" role="img" aria-label="Single room photo" style="background:linear-gradient(135deg,#e0d2bc,#9c7c5a)"></div><span class="type-btn">DETAILS</span></div>
      <div class="type"><div class="type-label">Twin</div><div class="type-photo" role="img" aria-label="Twin room photo" style="background:linear-gradient(135deg,#d9c8ae,#8f6f4e)"></div><span class="type-btn">DETAILS</span></div>
      <div class="type"><div class="type-label">Double</div><div class="type-photo" role="img" aria-label="Double room photo" style="background:linear-gradient(135deg,#e2d6c2,#a3876a)"></div><span class="type-btn">DETAILS</span></div>
    </div>
  </section>

  <section class="room">
    <div class="room-photo" role="img" aria-label="Cambodia room photo" style="background:linear-gradient(135deg,#b89870,#6e4a2c)"></div>
    <div class="room-body"><h2 class="room-name">Cambodia Room</h2><p class="room-text">Spacious and calm, this room opens onto the garden terrace with natural light through the day. Hand-finished teak furniture, soft linens and a rain shower bring comfort after long journeys across the province. Breakfast is served daily on the veranda.</p></div>
    <div class="room-types">
      <div class="type"><div class="type-label">Single</div><div class="type-photo" role="img" aria-label="Single room photo" style="background:linear-gradient(135deg,#c4a47c,#76502f)"></div><span class="type-btn">DETAILS</span></div>
      <div class="type"><div class="type-label">Twin</div><div class="type-photo" role="img" aria-label="Twin room photo" style="background:linear-gradient(135deg,#d4bc98,#8a6644)"></div><span class="type-btn">DETAILS</span></div>
      <div class="type"><div class="type-label">Double</div><div class="type-photo" role="img" aria-label="Double room photo" style="background:linear-gradient(135deg,#b8966c,#6a4628)"></div><span class="type-btn">DETAILS</span></div>
    </div>
  </section>

  <section class="room">
    <div class="room-photo" role="img" aria-label="Family room photo" style="background:linear-gradient(135deg,#c7ab88,#7a563a)"></div>
    <div class="room-body"><h2 class="room-name">Family Room</h2><p class="room-text">Spacious and calm, this room opens onto the garden terrace with natural light through the day. Hand-finished teak furniture, soft linens and a rain shower bring comfort after long journeys across the province. Breakfast is served daily on the veranda.</p></div>
    <div class="room-types">
      <div class="type"><div class="type-label">Single</div><div class="type-photo" role="img" aria-label="Family room detail photo" style="background:linear-gradient(135deg,#cdb290,#80603f)"></div><span class="type-btn">DETAILS</span></div>
    </div>
  </section>

  <section class="room">
    <div class="room-photo" role="img" aria-label="Junior suite photo" style="background:linear-gradient(135deg,#8e9aa8,#4c4038)"></div>
    <div class="room-body"><h2 class="room-name">Junior Suite</h2><p class="room-text">Spacious and calm, this room opens onto the garden terrace with natural light through the day. Hand-finished teak furniture, soft linens and a rain shower bring comfort after long journeys across the province. Breakfast is served daily on the veranda.</p></div>
    <div class="room-types">
      <div class="type"><div class="type-label">Single</div><div class="type-photo" role="img" aria-label="Junior suite detail photo" style="background:linear-gradient(135deg,#9aa4ae,#564a40)"></div><span class="type-btn">DETAILS</span></div>
    </div>
  </section>

  <section class="room">
    <div class="room-photo" role="img" aria-label="Suite photo" style="background:linear-gradient(135deg,#b0a898,#5a4636)"></div>
    <div class="room-body"><h2 class="room-name">Suite</h2><p class="room-text">Spacious and calm, this room opens onto the garden terrace with natural light through the day. Hand-finished teak furniture, soft linens and a rain shower bring comfort after long journeys across the province. Breakfast is served daily on the veranda.</p></div>
    <div class="room-types">
      <div class="type"><div class="type-label">Single</div><div class="type-photo" role="img" aria-label="Suite detail photo" style="background:linear-gradient(135deg,#b8ae9c,#604c3a)"></div><span class="type-btn">DETAILS</span></div>
    </div>
  </section>
</main>

<footer class="footer">
  <div class="fcol" style="left:90px">
    <h3>About Our Hotel</h3>
    <p>Velmora-Boutique Hotel sits among quiet hills, a short ride from the old market. Our team welcomes travellers seeking calm rooms, local cuisine and guided days in the countryside. Read more »</p>
  </div>
  <div class="fcol" style="left:280px">
    <h3>From Our Blog</h3>
    <div class="post"><div class="thumb" role="img" aria-label="Blog post thumbnail" style="background:#8a6a4a"></div><p><b>12.06.2013</b>New rooftop terrace opens for sunset dinners</p></div>
    <div class="post"><div class="thumb" role="img" aria-label="Blog post thumbnail" style="background:#6d7a5a"></div><p><b>23.05.2013</b>Guided river tours now available for guests</p></div>
  </div>
  <div class="fcol" style="left:455px">
    <div class="fbox">
      <div class="banner" role="img" aria-label="Hotel page cover photo"></div>
      <div class="caption">Find us</div>
      <div class="faces"><span></span><span></span><span></span><span></span><span></span><span></span></div>
    </div>
  </div>
  <div class="copyright">Copyright © 2013, Velmora-Boutique Hotel. All rights reserved. Design by Studio Marrow</div>
</footer>
</body>
</html>
```